Premium Honey Fusions need a label design. 5 awesome blends (see below)

We need a label design for a line of honey. Brand is an existing brand called MELVORIK. www.melvorikusa.example
MELVORIK is a line of juices. The honey line is an extension of the MELVORIK juice line.
Blends are:
Honey Cinnamon
Honey Saffron
Honey Ginger
Honey Herbs
Honey Wild Flower
PRODUCT FROM INDIA
We need a label design for a line of honey. Brand is an existing brand called MELVORIK.
See www.melvorikusa.example
We would like to see label designs that:
-are easy to read, clean
-"Honey Cinnamon”, etc... should be prominent, as it will be what will set us apart.
-use colors that communicate "premium honey"
-premium
-unique
-healthy/good for you
-We need a “Help us save the bees” type message on the logo. We will give % of profit from sale of honey to go towards saving the bees.
The final design should communicate :
-healthy
-DELICIOUS!!!! (it is!)
-premium
-unique
-exotic
Glass bottle is square (see pics) and label has 3 sides:
Front panel
Side panel 1: will be nutritional, ingredients, UPC, etc
Side panel 2: a story about bees? about saffron, about cinnamon??
Target Market(s)
Hispanic and American markets.
Healthy conscious people.
Premium honey market
Look and feel

```html
<!DOCTYPE html>
<html lang="en">
<head>
<meta charset="utf-8">
<title>MELVORIK Premium Honey – Label Line</title>
<link href="https://fonts.googleapis.com/css2?family=Alfa+Slab+One&family=Arimo:wght@400;700&family=Dancing+Script:wght@600&family=Rokkitt:wght@600&display=swap" rel="stylesheet">
<style>
  :root{
    --label-yellow:#f1e82e;
    --comb-yellow:#f4d93a;
    --honey-deep:#e39a1c;
    --honey-amber:#c8771a;
    --bark:#7a5a3c;
    --brand-red:#e21d24;
    --ink:#3b2a17;
    --cream:#f5e6bc;
    --badge-orange:#f0a030;
    --white:#ffffff;
  }
  *{box-sizing:border-box;margin:0;padding:0}
  html,body{width:1200px;height:1200px;overflow:hidden;background:var(--white)}
  body{position:relative;font-family:"Arimo",Arial,sans-serif;color:var(--ink)}

  /* ---------- flat label strip ---------- */
  .label{position:absolute;left:50px;width:450px;height:176px;background:var(--label-yellow);display:flex;overflow:hidden}
  .panel-facts{position:relative;width:138px;height:100%}
  .panel-front-slot{position:relative;width:180px;height:100%;overflow:hidden}
  .panel-story{position:relative;width:132px;height:100%;padding:10px 4px 0 8px}

  .importer{position:absolute;left:8px;top:10px;height:150px;writing-mode:vertical-rl;font-size:6.4px;line-height:8px;color:var(--ink)}
  .nutra-box{position:absolute;left:46px;top:12px;width:72px;height:154px;border:1px solid var(--ink);display:flex;align-items:center;justify-content:center;text-align:center;font-size:6.6px;line-height:7.6px;text-transform:uppercase}
  .upc-box{position:absolute;left:8px;top:108px;width:30px;height:60px;background:var(--white);display:flex;align-items:center;justify-content:center}
  .upc-box span{writing-mode:vertical-rl;font-size:6.2px;letter-spacing:.2px}

  .story-title{font-family:"Dancing Script",cursive;font-size:8px;line-height:10px}
  .story-copy{font-size:6.4px;line-height:7.8px;margin-bottom:16px}

  /* ---------- front panel (drawn at 448 × 486, scaled for strips) ---------- */
  .front{position:absolute;left:0;top:0;width:448px;height:486px;overflow:hidden;
    background:linear-gradient(160deg,#f7e65a 0%,var(--comb-yellow) 55%,#f0c93a 100%)}
  .panel-front-slot .front{transform:scale(.402);transform-origin:0 0}
  .front-shapes{position:absolute;inset:0;width:100%;height:100%}
  .pledge{position:absolute;left:8px;top:6px;width:150px;font-family:"Dancing Script",cursive;font-size:11px;line-height:12px;color:var(--cream)}
  .badge{position:absolute;left:40px;top:56px;width:100px;height:100px;border-radius:50%;background:var(--badge-orange);
    box-shadow:0 0 0 5px var(--bark), inset 0 0 0 4px var(--cream);
    display:flex;align-items:center;justify-content:center;text-align:center;
    font-family:"Alfa Slab One",serif;font-size:14px;line-height:15px;color:var(--ink)}
  .badge b{font-size:20px;display:block;line-height:22px;font-weight:400}
  .brand{position:absolute;left:146px;top:84px;width:240px;text-align:center;font-family:"Arimo",sans-serif;font-weight:700;font-size:40px;color:var(--brand-red);letter-spacing:1px}
  .premium{position:absolute;left:148px;top:146px;width:180px;text-align:center;font-family:"Alfa Slab One",serif;font-size:19px;line-height:22px;color:var(--bark);letter-spacing:1px}
  .honey{position:absolute;left:66px;top:164px;width:340px;text-align:center;font-family:"Alfa Slab One",serif;font-size:84px;line-height:88px;color:var(--brand-red);
    text-shadow:3px 0 0 var(--white),-3px 0 0 var(--white),0 3px 0 var(--white),0 -3px 0 var(--white),6px 6px 0 var(--bark)}
  .flavor{position:absolute;left:80px;top:258px;width:320px;text-align:center;font-family:"Rokkitt",serif;font-weight:600;font-size:42px;line-height:46px;letter-spacing:2px;color:var(--cream);transform:rotate(-15deg);transform-origin:50% 50%}
  .flavor.long{font-size:32px}
  .art{position:absolute;left:0;top:318px;width:330px;height:168px;border-radius:0 58% 0 0 / 0 70% 0 0;
    background:linear-gradient(135deg,var(--art-a) 0%,var(--art-b) 100%)}
  .dipper{position:absolute;left:404px;top:18px;width:34px;height:128px;border-radius:6px 6px 17px 17px;
    background:linear-gradient(180deg,#d9a050 0%,var(--honey-amber) 100%)}

  .cinnamon{--ribbon:#8a6a4a;--art-a:#8a4a22;--art-b:#d98a20}
  .saffron{--ribbon:#6b5bb0;--art-a:#6a5aa8;--art-b:#e39a1c}
  .herbs{--ribbon:#3aa548;--art-a:#4f8a2a;--art-b:#e39a1c}
  .ginger{--ribbon:#a08a6a;--art-a:#d8b77a;--art-b:#e39a1c}
  .wildflowers{--ribbon:#3aa548;--art-a:#e0608a;--art-b:#f08a20}

  /* ---------- enlarged front panel ---------- */
  .hero-front{position:absolute;left:632px;top:366px;width:448px;height:486px}
</style>
</head>
<body>

<section class="label cinnamon" style="top:58px">
  <div class="panel-facts">
    <p class="importer">Harbor Crest Imports USA, Inc<br>2210 N Alder St<br>Brookfield, PA 18000<br>melvorikusa.example</p>
    <div class="nutra-box">Placement<br>for<br>nutra facts</div>
    <div class="upc-box"><span>UPC CODE</span></div>
  </div>
  <div class="panel-front-slot">
    <div class="front">
      <svg class="front-shapes" viewBox="0 0 448 486" preserveAspectRatio="none" aria-hidden="true">
        <polygon points="0,0 190,0 0,140" fill="var(--bark)"/>
        <path d="M0 250 C140 290 300 250 440 180 L448 250 C320 330 160 350 0 340 Z" fill="var(--ribbon)"/>
      </svg>
      <p class="pledge">We will give 00% of profit from<br>sale of honey to go<br>towards saving<br>the BEES</p>
      <div class="badge"><span>HELP US<br>SAVE THE<b>BEES</b></span></div>
      <div class="dipper" role="img" aria-label="Wooden honey dipper dripping honey"></div>
      <div class="brand">MELVORIK</div>
      <div class="premium">PREMIUM</div>
      <div class="honey">HONEY</div>
      <div class="art" role="img" aria-label="Cinnamon sticks and cloves in a pool of honey"></div>
      <div class="flavor">CINNAMON</div>
    </div>
  </div>
  <div class="panel-story">
    <p class="story-title">Story about Bees</p>
    <p class="story-copy">Copy to come Copy to come<br>Copy to come Copy to come<br>Copy to come Copy to come<br>Copy to come Copy to come<br>Copy to come Copy to come<br>Copy to come Copy to come<br>Copy to come Copy to come<br>Copy to come Copy to come</p>
    <p class="story-title">About cinnamon</p>
    <p class="story-copy">Copy to come Copy to come<br>Copy to come Copy to come<br>Copy to come Copy to come<br>Copy to come Copy to come</p>
  </div>
</section>

<section class="label saffron" style="top:277px">
  <div class="panel-facts">
    <p class="importer">Harbor Crest Imports USA, Inc<br>2210 N Alder St<br>Brookfield, PA 18000<br>melvorikusa.example</p>
    <div class="nutra-box">Placement<br>for<br>nutra facts</div>
    <div class="upc-box"><span>UPC CODE</span></div>
  </div>
  <div class="panel-front-slot">
    <div class="front">
      <svg class="front-shapes" viewBox="0 0 448 486" preserveAspectRatio="none" aria-hidden="true">
        <polygon points="0,0 190,0 0,140" fill="var(--bark)"/>
        <path d="M0 250 C140 290 300 250 440 180 L448 250 C320 330 160 350 0 340 Z" fill="var(--ribbon)"/>
      </svg>
      <p class="pledge">We will give 00% of profit from<br>sale of honey to go<br>towards saving<br>the BEES</p>
      <div class="badge"><span>HELP US<br>SAVE THE<b>BEES</b></span></div>
      <div class="dipper" role="img" aria-label="Wooden honey dipper dripping honey"></div>
      <div class="brand">MELVORIK</div>
      <div class="premium">PREMIUM</div>
      <div class="honey">HONEY</div>
      <div class="art" role="img" aria-label="Saffron crocus flowers over a pool of honey"></div>
      <div class="flavor">SAFRON</div>
    </div>
  </div>
  <div class="panel-story">
    <p class="story-title">Story about Bees</p>
    <p class="story-copy">Copy to come Copy to come<br>Copy to come Copy to come<br>Copy to come Copy to come<br>Copy to come Copy to come<br>Copy to come Copy to come<br>Copy to come Copy to come<br>Copy to come Copy to come<br>Copy to come Copy to come</p>
    <p class="story-title">About safron</p>
    <p class="story-copy">Copy to come Copy to come<br>Copy to come Copy to come<br>Copy to come Copy to come<br>Copy to come Copy to come</p>
  </div>
</section>

<section class="label herbs" style="top:507px">
  <div class="panel-facts">
    <p class="importer">Harbor Crest Imports USA, Inc<br>2210 N Alder St<br>Brookfield, PA 18000<br>melvorikusa.example</p>
    <div class="nutra-box">Placement<br>for<br>nutra facts</div>
    <div class="upc-box"><span>UPC CODE</span></div>
  </div>
  <div class="panel-front-slot">
    <div class="front">
      <svg class="front-shapes" viewBox="0 0 448 486" preserveAspectRatio="none" aria-hidden="true">
        <polygon points="0,0 190,0 0,140" fill="var(--bark)"/>
        <path d="M0 250 C140 290 300 250 440 180 L448 250 C320 330 160 350 0 340 Z" fill="var(--ribbon)"/>
      </svg>
      <p class="pledge">We will give 00% of profit from<br>sale of honey to go<br>towards saving<br>the BEES</p>
      <div class="badge"><span>HELP US<br>SAVE THE<b>BEES</b></span></div>
      <div class="dipper" role="img" aria-label="Wooden honey dipper dripping honey"></div>
      <div class="brand">MELVORIK</div>
      <div class="premium">PREMIUM</div>
      <div class="honey">HONEY</div>
      <div class="art" role="img" aria-label="Fresh rosemary and parsley sprigs over a pool of honey"></div>
      <div class="flavor">HERBS</div>
    </div>
  </div>
  <div class="panel-story">
    <p class="story-title">Story about Bees</p>
    <p class="story-copy">Copy to come Copy to come<br>Copy to come Copy to come<br>Copy to come Copy to come<br>Copy to come Copy to come<br>Copy to come Copy to come<br>Copy to come Copy to come<br>Copy to come Copy to come<br>Copy to come Copy to come</p>
    <p class="story-title">About cinnamon</p>
    <p class="story-copy">Copy to come Copy to come<br>Copy to come Copy to come<br>Copy to come Copy to come<br>Copy to come Copy to come</p>
  </div>
</section>

<section class="label ginger" style="top:741px">
  <div class="panel-facts">
    <p class="importer">Harbor Crest Imports USA, Inc<br>2210 N Alder St<br>Brookfield, PA 18000<br>melvorikusa.example</p>
    <div class="nutra-box">Placement<br>for<br>nutra facts</div>
    <div class="upc-box"><span>UPC CODE</span></div>
  </div>
  <div class="panel-front-slot">
    <div class="front">
      <svg class="front-shapes" viewBox="0 0 448 486" preserveAspectRatio="none" aria-hidden="true">
        <polygon points="0,0 190,0 0,140" fill="var(--bark)"/>
        <path d="M0 250 C140 290 300 250 440 180 L448 250 C320 330 160 350 0 340 Z" fill="var(--ribbon)"/>
      </svg>
      <p class="pledge">We will give 00% of profit from<br>sale of honey to go<br>towards saving<br>the BEES</p>
      <div class="badge"><span>HELP US<br>SAVE THE<b>BEES</b></span></div>
      <div class="dipper" role="img" aria-label="Wooden honey dipper dripping honey"></div>
      <div class="brand">MELVORIK</div>
      <div class="premium">PREMIUM</div>
      <div class="honey">HONEY</div>
      <div class="art" role="img" aria-label="Ginger root in a pool of honey"></div>
      <div class="flavor">GINGER</div>
    </div>
  </div>
  <div class="panel-story">
    <p class="story-title">Story about Bees</p>
    <p class="story-copy">Copy to come Copy to come<br>Copy to come Copy to come<br>Copy to come Copy to come<br>Copy to come Copy to come<br>Copy to come Copy to come<br>Copy to come Copy to come<br>Copy to come Copy to come<br>Copy to come Copy to come</p>
    <p class="story-title">About cinnamon</p>
    <p class="story-copy">Copy to come Copy to come<br>Copy to come Copy to come<br>Copy to come Copy to come<br>Copy to come Copy to come</p>
  </div>
</section>

<section class="label wildflowers" style="top:998px">
  <div class="panel-facts">
    <p class="importer">Harbor Crest Imports USA, Inc<br>2210 N Alder St<br>Brookfield, PA 18000<br>melvorikusa.example</p>
    <div class="nutra-box">Placement<br>for<br>nutra facts</div>
    <div class="upc-box"><span>UPC CODE</span></div>
  </div>
  <div class="panel-front-slot">
    <div class="front">
      <svg class="front-shapes" viewBox="0 0 448 486" preserveAspectRatio="none" aria-hidden="true">
        <polygon points="0,0 190,0 0,140" fill="var(--bark)"/>
        <path d="M0 250 C140 290 300 250 440 180 L448 250 C320 330 160 350 0 340 Z" fill="var(--ribbon)"/>
      </svg>
      <p class="pledge">We will give 00% of profit from<br>sale of honey to go<br>towards saving<br>the BEES</p>
      <div class="badge"><span>HELP US<br>SAVE THE<b>BEES</b></span></div>
      <div class="dipper" role="img" aria-label="Wooden honey dipper dripping honey"></div>
      <div class="brand">MELVORIK</div>
      <div class="premium">PREMIUM</div>
      <div class="honey">HONEY</div>
      <div class="art" role="img" aria-label="Bouquet of pink and orange wild flowers"></div>
      <div class="flavor long">WILD FLOWERS</div>
    </div>
  </div>
  <div class="panel-story">
    <p class="story-title">Story about Bees</p>
    <p class="story-copy">Copy to come Copy to come<br>Copy to come Copy to come<br>Copy to come Copy to come<br>Copy to come Copy to come<br>Copy to come Copy to come<br>Copy to come Copy to come<br>Copy to come Copy to come<br>Copy to come Copy to come</p>
    <p class="story-title">About cinnamon</p>
    <p class="story-copy">Copy to come Copy to come<br>Copy to come Copy to come<br>Copy to come Copy to come<br>Copy to come Copy to come</p>
  </div>
</section>

<section class="hero-front cinnamon" aria-label="Cinnamon front panel">
  <div class="front">
    <svg class="front-shapes" viewBox="0 0 448 486" preserveAspectRatio="none" aria-hidden="true">
      <polygon points="0,0 190,0 0,140" fill="var(--bark)"/>
      <path d="M0 250 C140 290 300 250 440 180 L448 250 C320 330 160 350 0 340 Z" fill="var(--ribbon)"/>
    </svg>
    <p class="pledge">We will give 00% of profit from<br>sale of honey to go<br>towards saving<br>the BEES</p>
    <div class="badge"><span>HELP US<br>SAVE THE<b>BEES</b></span></div>
    <div class="dipper" role="img" aria-label="Wooden honey dipper dripping honey"></div>
    <div class="brand">MELVORIK</div>
    <div class="premium">PREMIUM</div>
    <div class="honey">HONEY</div>
    <div class="art" role="img" aria-label="Cinnamon sticks and cloves in a pool of honey"></div>
    <div class="flavor">CINNAMON</div>
  </div>
</section>

</body>
</html>
```